Security and Technology Website - Bold and Confident, Something Unexpected

Silver Heron Systems is launching its first website and we need a great design to bring our brand to life and generate DTC and B2B leads.

We have a good logo, but I am struggling with the creative vision to bring it all together. While our industry is Alarm Systems and Technology, we want to create a site that is more friendly and less 'typical' than your standard IT sites.

It Must:
1. Appeal to both men and women. The logo is a bit masculine, so the colors and icons must soften this.
2. Feel modern - we need to convey that we we use the latest technology.
3. Feel a bit high-end. We are not a budget solution.
4. Have a distinct iconography and photo treatment.
5. Feel layered - not just a series of stacked horizontal modules.

It Should Not:
1. Feel like your typical IT website.

Here are resources to get you started!
• Staging Site:
https://silver-heron-systems.examplestore.test/
Password: Pippa

•Brand Guide: https://www.sketchboardly.test/design/QWRtLmPOx4K/vBnm8Kq2-ZXyTrLp7hd-QE/edit?utm_content=QWRtLmPOx4K&utm_campaign=designshare&utm_medium=link2&utm_source=sharebutton

• Logo and Fonts and Photos: :https://files.cloudvaultia.test/folders/7KpWmQ3xNrT8yLbZ2vHcJ5dFg9sAeUoPi?usp=sharing

• Design Inspiration (don't feel limited by this): https://www.sketchboardly.test/design/HJkPqRvBn2s/m7TyUiOp4LkJhGfDsA2-ZX/edit?utm_content=HJkPqRvBn2s&utm_campaign=designshare&utm_medium=link2&utm_source=sharebutton

______________

The winner will be asked to provide design files and finished PNGs of the overall design file, backgrounds, photo treatments/frames, and icons.

The winner will likely be engaged for a phase 2 to build out a product page.

Industry/Entity Type

Alarm Systems, Home Theatres, and Commercial IT Networking

Number of Pages Required

1 page

Font styles to use
Sans Serif

Colors
0054AA
0677BA
7BADD7
CADEEF
E8F1F8
0094D4
00A9DD
6FCCEA
C7EBF8
E9F6FB
EB3D1F
EC4F4E
F09395
F8D3D4
FCEDEE

Requirements
Must have
• 1. Appeal to both men and women. The logo is a bit masculine, so the colors and icons must soften this. 2. Feel modern - we need to convey that we we use the latest technology. 3. Feel a bit high-end. We are not a budget solution. 4. Have a distinct iconography and photo treatment. 5. Feel layered - not just a series of stacked horizontal modules.
Should not have
• 1. Should not feel like just another IT website.

```html
<!DOCTYPE html>
<html lang="en">
<head>
<meta charset="utf-8">
<title>Silver Heron Systems</title>
<link href="https://fonts.googleapis.com/css2?family=Lexend+Exa:wght@300;400&family=Michroma&family=Montserrat:wght@400;500;600;700&display=swap" rel="stylesheet">
<style>
:root{
  --navy:#0054AA; --blue:#0677BA; --sky:#0094D4; --cyan:#00A9DD; --aqua:#6FCCEA;
  --ice:#C7EBF8; --mist:#E9F6FB; --steel:#7BADD7; --pale:#CADEEF;
  --red:#EB3D1F; --rose:#EC4F4E; --blush:#F09395; --pink:#F8D3D4; --petal:#FCEDEE;
  --ink:#1d2433; --text:#3d4452; --dark:#0b1a33;
}
*{box-sizing:border-box;margin:0;padding:0}
html,body{width:1200px;height:5333px;overflow:hidden;background:#fff}
body{position:relative;font-family:"Montserrat",sans-serif;color:var(--text)}
.abs{position:absolute}
.display{font-family:"Lexend Exa",sans-serif;font-weight:300;letter-spacing:-1px;text-transform:uppercase;line-height:1.15;white-space:nowrap}
.label{font-family:"Michroma",sans-serif;text-transform:uppercase}
.btn{position:absolute;display:flex;align-items:center;justify-content:center;font-family:"Michroma",sans-serif;font-size:11px;text-transform:uppercase;color:#fff;background:var(--red);white-space:nowrap}
.btn.outline{background:transparent;border:2px solid var(--ink);color:var(--ink)}
.photo{position:absolute}
/* nav */
.logo-box{left:83px;top:0;width:103px;height:87px;background:#fff;display:flex;align-items:center;justify-content:center;text-align:center;font-family:"Michroma",sans-serif;font-size:10px;color:var(--navy);line-height:1.4;padding:6px}
.nav{left:228px;top:38px;display:flex;gap:16px;font-family:"Michroma",sans-serif;font-size:9px;color:#fff;white-space:nowrap}
/* cards */
.card{position:absolute;background:#fff;box-shadow:0 4px 18px rgba(0,0,0,.12)}
.card .img{height:var(--ih)}
.card h3{font-family:"Michroma",sans-serif;font-size:13px;font-weight:400;text-transform:uppercase;color:var(--sky);margin:36px 0 0 25px;white-space:nowrap}
.card p{font-size:11px;line-height:1.55;margin:10px 25px 0;color:var(--text)}
.more{font-size:11px;color:var(--red);margin:16px 25px 0;display:block}
.more::after{content:"  →"}
/* features */
.feature{position:absolute;width:190px}
.feature h4{font-family:"Michroma",sans-serif;font-size:12px;font-weight:400;text-transform:uppercase;color:var(--ink);line-height:1.5;margin-top:14px;white-space:nowrap}
.feature p{font-size:10px;line-height:1.5;margin-top:8px}
.feature .more{margin:12px 0 0;font-size:10px}
/* testimonials */
.quote{position:absolute;width:334px;height:197px;background:#fff;box-shadow:0 4px 18px rgba(0,0,0,.12)}
.quote .avatar{position:absolute;left:22px;top:60px;width:72px;height:72px;border-radius:50%;background:linear-gradient(135deg,var(--pale),#b9a48c)}
.quote .name{position:absolute;left:112px;top:34px;font-size:11px;font-weight:700;color:var(--ink)}
.quote .stars{position:absolute;left:200px;top:30px;color:#f5a623;font-size:15px;letter-spacing:3px}
.quote p{position:absolute;left:112px;top:62px;width:200px;font-size:13px;line-height:1.5}
/* form */
.field{position:absolute;background:#fff;font-size:12px;color:#666;padding:12px 16px}
/* footer */
.foot h5{font-family:"Michroma",sans-serif;font-size:16px;font-weight:400;text-transform:uppercase;color:var(--ink);white-space:nowrap}
.foot li{list-style:none;font-size:12px;line-height:25px}
.social{position:absolute;top:5152px;width:34px;height:34px;border-radius:50%}
</style>
</head>
<body>

<!-- HERO -->
<section class="abs" style="left:0;top:0;width:1200px;height:600px;background:linear-gradient(90deg,var(--aqua) 0%,#8fd4f0 45%,var(--ice) 100%)">
  <div class="photo" role="img" aria-label="Woman using a wall-mounted security touch panel at home" style="left:640px;top:0;width:560px;height:600px;background:linear-gradient(90deg,rgba(143,212,240,0) 0%,#c9d6df 40%,#9fb3c4 100%)"></div>
</section>
<div class="abs logo-box">Silver Heron Systems</div>
<nav class="abs nav"><span>HOME</span><span>ELECTRONIC SECURITY</span><span>AUDIO+VIDEO</span><span>NETWORKING+COMMUNICATION</span><span>CABLING</span></nav>
<svg class="abs" style="left:926px;top:34px" width="18" height="18" viewBox="0 0 18 18"><circle cx="7.5" cy="7.5" r="6" fill="none" stroke="#fff" stroke-width="2"/><line x1="12" y1="12" x2="17" y2="17" stroke="#fff" stroke-width="2"/></svg>
<div class="btn" style="left:964px;top:29px;width:153px;height:33px">Contact Us</div>
<h1 class="abs display" style="left:83px;top:152px;font-size:42px;color:var(--navy)">Protect your world<br>with the latest<br>security technology</h1>
<p class="abs" style="left:83px;top:316px;width:620px;font-size:13px;line-height:1.6;color:var(--ink)">Lorem ipsum dolor sit amet, consectetur adipiscing elit. Aliquam nec facilisis nisl.Lorem ipsum dolor sitLorem ipsum dolor sit amet, consectetur adipiscing elit. Aliquam nec facilisis nisl.Lorem ipsum dolor sit amet, consectetur adipiscing elit. Aliquam</p>
<div class="btn" style="left:83px;top:400px;width:153px;height:34px">Get a Quote</div>
<div class="btn outline" style="left:258px;top:400px;width:222px;height:34px">Free Consultation</div>

<!-- ABOUT -->
<svg class="abs" style="left:97px;top:683px" width="445" height="527" viewBox="0 0 445 527" role="img" aria-label="Woman setting an alarm keypad by the front door">
  <defs><linearGradient id="gAbout" x1="0" y1="0" x2="1" y2="1"><stop offset="0" stop-color="#d9cfc4"/><stop offset="1" stop-color="#a8948a"/></linearGradient></defs>
  <path d="M222 4 L441 58 L441 330 L222 523 L4 330 L4 58 Z" fill="url(#gAbout)" stroke="#0094D4" stroke-width="6"/>
</svg>
<svg class="abs" style="left:393px;top:1003px" width="182" height="218" viewBox="0 0 182 218" role="img" aria-label="Portrait of the company founder">
  <path d="M91 4 L178 30 L178 140 L91 214 L4 140 L4 30 Z" fill="#1f3550" stroke="#0094D4" stroke-width="5"/>
</svg>
<div class="abs" style="left:627px;top:784px;font-size:14px;color:var(--ink)">About Us</div>
<h2 class="abs display" style="left:627px;top:815px;font-size:40px;color:var(--navy)">Who we are</h2>
<p class="abs label" style="left:627px;top:875px;font-size:10.5px;line-height:1.6;color:var(--sky);white-space:nowrap">I founded Silver Heron Systems to bring together<br>technology and honest, reliable service.</p>
<p class="abs" style="left:627px;top:932px;width:470px;font-size:13px;line-height:1.6;color:var(--ink)">I’m proud to call Tennessee home and even prouder to help keep its homes and businesses secure.<br>Whether it’s protecting or elevating your space, my goal is to make technology work for you.<br>Think of us as your friendly, neighborhood tech expert—here to safeguard what matters most.</p>
<div class="btn" style="left:627px;top:1076px;width:275px;height:35px">Tell us how we can help</div>
<div class="btn outline" style="left:919px;top:1076px;width:157px;height:35px">Learn More</div>

<!-- ELECTRONIC SECURITY -->
<section class="abs" role="img" aria-label="Modern home exterior lit at dusk" style="left:0;top:1308px;width:1200px;height:575px;background:linear-gradient(180deg,#0b1a33 0%,#14284a 60%,#2a3d5a 100%)"></section>
<h2 class="abs display" style="left:0;top:1384px;width:1200px;text-align:center;font-size:40px;color:var(--cyan)">Electronic Security</h2>
<p class="abs" style="left:270px;top:1447px;width:660px;text-align:center;font-size:13px;line-height:1.6;color:#fff">Lorem ipsum dolor sit amet, consectetur adipiscing elit. Aliquam nec facilisis nisl.Lorem ipsum dolor sitLorem ipsum dolor sit amet, consectetur adipiscing elit. Aliquam nec facilisis nisl.Lorem</p>
<div class="card" style="left:83px;top:1512px;width:333px;height:423px;--ih:216px"><div class="img" role="img" aria-label="Woman using a home alarm panel" style="background:linear-gradient(135deg,#e6ded6,#b59e90)"></div><h3>Affordable Security</h3><p>Lorem ipsum dolor sit amet, consectetur adipiscing elit. Aliquam nec facilisis nisl.Lorem ipsum dolor sitLorem ipsum dolor sit amet, consectetur adipiscing elit. Aliquam nec facilisis</p><span class="more">Learn more</span></div>
<div class="card" style="left:432px;top:1512px;width:334px;height:423px;--ih:216px"><div class="img" role="img" aria-label="Wall-mounted television in a living room" style="background:linear-gradient(135deg,#c9b9a6,#6e6a70)"></div><h3>Enviable Entertainment</h3><p>Lorem ipsum dolor sit amet, consectetur adipiscing elit. Aliquam nec facilisis nisl.Lorem ipsum dolor sitLorem ipsum dolor sit amet, consectetur adipiscing elit. Aliquam nec facilisis</p><span class="more">Learn more</span></div>
<div class="card" style="left:782px;top:1512px;width:335px;height:423px;--ih:216px"><div class="img" role="img" aria-label="Team on a video conference in an office" style="background:linear-gradient(135deg,#dfe6ee,#7d8a99)"></div><h3>Connected Businesses</h3><p>Lorem ipsum dolor sit amet, consectetur adipiscing elit. Aliquam nec facilisis nisl.Lorem ipsum dolor sitLorem ipsum dolor sit amet, consectetur adipiscing elit. Aliquam nec facilisis</p><span class="more">Learn more</span></div>
<div class="btn" style="left:534px;top:1966px;width:132px;height:35px">See More</div>

<!-- CONNECT + PROTECT -->
<section class="abs" style="left:0;top:2028px;width:1200px;height:434px;background:linear-gradient(180deg,#fff 0%,var(--petal) 25%,var(--mist) 70%,#fff 100%)"></section>
<h2 class="abs display" style="left:0;top:2075px;width:1200px;text-align:center;font-size:38px;color:var(--sky)">Connect + protect your world</h2>
<p class="abs label" style="left:0;top:2139px;width:1200px;text-align:center;font-size:11px;color:var(--navy)">Protect your people, assets, and information from whatever comes</p>

<svg width="0" height="0" style="position:absolute"><defs>
<symbol id="shield" viewBox="0 0 88 104"><path d="M44 3 L85 16 L85 64 L44 100 L3 64 L3 16 Z" fill="#fff" stroke="#EB3D1F" stroke-width="3"/></symbol>
</defs></svg>

<div class="feature" style="left:101px;top:2177px"><svg width="88" height="104"><use href="#shield"/><rect x="34" y="32" width="22" height="32" fill="#EB3D1F"/><path d="M26 48 h14 m-5 -5 l5 5 l-5 5" stroke="#EB3D1F" stroke-width="3" fill="none"/></svg><h4>Entry &amp; Motion<br>Sensors</h4><p>Lorem ipsum dolor sit amet, consectetur adipiscing elit. Aliquam nec facilisis nisl.Lo</p><span class="more">Learn more</span></div>
<div class="feature" style="left:312px;top:2177px"><svg width="88" height="104"><use href="#shield"/><rect x="32" y="28" width="22" height="38" rx="4" fill="#EB3D1F"/><circle cx="43" cy="52" r="5" fill="#fff"/><path d="M60 40 q5 8 0 16 M65 36 q8 12 0 24" stroke="#EB3D1F" stroke-width="2.5" fill="none"/></svg><h4>Video<br>Doorbells</h4><p>Lorem ipsum dolor sit amet, consectetur adipiscing elit. Aliquam nec facilisis nisl.Lo</p><span class="more">Learn more</span></div>
<div class="feature" style="left:526px;top:2177px"><svg width="88" height="104"><use href="#shield"/><rect x="26" y="32" width="34" height="20" rx="3" fill="#EB3D1F"/><rect x="36" y="52" width="8" height="14" fill="#EB3D1F"/><rect x="28" y="64" width="18" height="4" fill="#EB3D1F"/></svg><h4>Security<br>Cameras</h4><p>Lorem ipsum dolor sit amet, consectetur adipiscing elit. Aliquam nec facilisis nisl.Lo</p><span class="more">Learn more</span></div>
<div class="feature" style="left:737px;top:2177px"><svg width="88" height="104"><use href="#shield"/><path d="M44 66 C20 50 26 30 38 34 C42 36 44 40 44 40 C44 40 46 36 50 34 C62 30 68 50 44 66 Z" fill="#EB3D1F"/></svg><h4>&nbsp;&nbsp;&nbsp;Pet<br>Friendly</h4><p>Lorem ipsum dolor sit amet, consectetur adipiscing elit. Aliquam nec facilisis nisl.Lo</p><span class="more">Learn more</span></div>
<div class="feature" style="left:948px;top:2177px"><svg width="88" height="104"><use href="#shield"/><path d="M44 26 C52 38 58 44 58 54 C58 63 52 68 44 68 C36 68 30 63 30 54 C30 46 36 42 38 36 C40 42 42 44 44 44 C44 38 42 32 44 26 Z" fill="#EB3D1F"/></svg><h4>Fire &amp; Carbon<br>Monoxide</h4><p>Lorem ipsum dolor sit amet, consectetur adipiscing elit. Aliquam nec facilisis nisl.Lo</p><span class="more">Learn more</span></div>
<div class="btn" style="left:523px;top:2472px;width:154px;height:36px">Contact Us</div>

<!-- SAFER HOME -->
<section class="abs" role="img" aria-label="Bright home interior backdrop" style="left:0;top:2593px;width:1200px;height:655px;background:linear-gradient(90deg,#fff 0%,#fff 40%,#b9d3ea 75%,#e2ded7 100%);opacity:.9"></section>
<section class="abs" style="left:0;top:2920px;width:1200px;height:328px;background:linear-gradient(180deg,rgba(255,255,255,0),#fff 60%)"></section>
<h2 class="abs display" style="left:83px;top:2596px;font-size:40px;color:var(--sky);line-height:1.25">A safer home or<br>business is as easy as</h2>
<p class="abs" style="left:83px;top:2705px;width:560px;font-size:13px;line-height:1.6;color:var(--ink)">Lorem ipsum dolor sit amet, consectetur adipiscing elit. Aliquam nec facilisis nisl.Lorem ipsum dolor sitLorem ipsum dolor sit amet, consectetur adipiscing elit. Aliquam nec facilisis nisl.Lorem ipsum dolor sitLorem ipsum dolor sit amet,</p>
<div class="card" style="left:83px;top:2797px;width:333px;height:362px;--ih:187px"><div class="img" role="img" aria-label="Couple planning together at a laptop" style="background:linear-gradient(135deg,#d8d1c8,#6c6660)"></div><h3>Build an Instant Quote</h3><p>Our live-estimate builder will guide you through a few questions to help us understand your needsOur live-estimate builder will guide you</p><span class="more">Learn more</span></div>
<div class="card" style="left:432px;top:2797px;width:334px;height:362px;--ih:187px"><div class="img" role="img" aria-label="Technician meeting clients in a brick-walled room" style="background:linear-gradient(135deg,#c97a55,#e6e0da)"></div><h3>Schedule Installation</h3><p>Our trained techs are efficient and friendly. Southern-born and raised (and one mid-westerner), we will respect your home and your schedule</p><span class="more">Learn more</span></div>
<div class="card" style="left:782px;top:2797px;width:335px;height:362px;--ih:187px"><div class="img" role="img" aria-label="Hands over a keyboard with a glowing home security symbol" style="background:linear-gradient(135deg,#2a3a55,#7b8fa8)"></div><h3>Stay Secure 24/7</h3><p>Monitor your home through the app, receive instant alerts, and rely on professional monitoring services for emergencies</p><span class="more">Learn more</span></div>
<div class="btn" style="left:517px;top:3190px;width:166px;height:36px">Get Started</div>

<!-- TESTIMONIALS -->
<section class="abs" role="img" aria-label="Smart home devices on a table" style="left:0;top:3500px;width:1200px;height:421px;background:linear-gradient(180deg,#fff 0%,#c5d3e4 40%,#5c6c86 100%)"></section>
<h2 class="abs display" style="left:0;top:3302px;width:1200px;text-align:center;font-size:40px;color:var(--sky);line-height:1.25">What client says<br>about us</h2>
<svg class="abs" style="left:445px;top:3459px" width="310" height="369" viewBox="0 0 310 369" role="img" aria-label="Woman on a video call in a home office">
  <path d="M155 5 L305 50 L305 240 L155 364 L5 240 L5 50 Z" fill="#3d4c66" stroke="#0094D4" stroke-width="8"/>
</svg>
<div class="quote" style="left:83px;top:3424px"><div class="avatar"></div><div class="name">Lorem</div><div class="stars">★★★★★</div><p>“ Lorem ipsum dolor sit amet consectetur. Mi nibh id quam sit iaculis sit in montes felis. Malesuada augue quis duis odio.”</p></div>
<div class="quote" style="left:83px;top:3652px"><div class="avatar"></div><div class="name">Lorem</div><div class="stars">★★★★★</div><p>“ Lorem ipsum dolor sit amet consectetur. Mi nibh id quam sit iaculis sit in montes felis. Malesuada augue quis duis odio.”</p></div>
<div class="quote" style="left:782px;top:3424px"><div class="avatar"></div><div class="name">Lorem</div><div class="stars">★★★★★</div><p>“ Lorem ipsum dolor sit amet consectetur. Mi nibh id quam sit iaculis sit in montes felis. Malesuada augue quis duis odio.”</p></div>
<div class="quote" style="left:782px;top:3652px"><div class="avatar"></div><div class="name">Lorem</div><div class="stars">★★★★★</div><p>“ Lorem ipsum dolor sit amet consectetur. Mi nibh id quam sit iaculis sit in montes felis. Malesuada augue quis duis odio.”</p></div>

<!-- REGISTRATION -->
<section class="abs" style="left:393px;top:4030px;width:807px;height:449px;background:linear-gradient(90deg,var(--rose) 0%,var(--blush) 35%,var(--steel) 75%,var(--aqua) 100%)"></section>
<svg class="abs" style="left:83px;top:4003px" width="476" height="538" viewBox="0 0 476 538" role="img" aria-label="Home theater room with large screen and recliners">
  <defs><linearGradient id="gTheatre" x1="0" y1="0" x2="1" y2="1"><stop offset="0" stop-color="#c98a45"/><stop offset="0.5" stop-color="#8a6a4e"/><stop offset="1" stop-color="#3a2c24"/></linearGradient></defs>
  <path d="M238 6 L470 72 L470 350 L238 532 L6 350 L6 72 Z" fill="url(#gTheatre)" stroke="#0094D4" stroke-width="10"/>
</svg>
<h2 class="abs display" style="left:633px;top:4063px;font-size:40px;color:var(--ink)">Registration</h2>
<div class="field" style="left:633px;top:4123px;width:472px;height:40px">Your Name</div>
<div class="field" style="left:633px;top:4176px;width:230px;height:41px">E-Mail</div>
<div class="field" style="left:879px;top:4176px;width:226px;height:41px">Phone</div>
<div class="field" style="left:633px;top:4231px;width:472px;height:39px">Company</div>
<div class="field" style="left:633px;top:4285px;width:472px;height:105px">Type Here</div>
<div class="btn" style="left:633px;top:4417px;width:159px;height:36px">Submit Now</div>

<!-- PARTNERS -->
<div class="abs" style="left:0;top:4685px;width:1200px;display:flex;justify-content:space-around;padding:0 70px;font-family:'Michroma',sans-serif;font-size:22px;color:var(--ink)">
  <span>Gatewright</span><span>Clearlens</span><span>Lockmere</span><span>Sonavale</span><span>Pathvane</span>
</div>

<!-- SUBSCRIBE -->
<div class="abs" style="left:244px;top:4890px;width:201px;text-align:center;font-family:'Michroma',sans-serif;font-size:20px;line-height:1.4;color:var(--ink)">Silver Heron Systems</div>
<div class="abs" style="left:494px;top:4886px;font-size:16px;color:var(--ink)">Subscribe Your News Latter Solutions?</div>
<div class="field" style="left:494px;top:4920px;width:323px;height:46px;border:1px solid #ccc;font-size:12px;color:#999">Enter Your Email</div>
<div class="btn" style="left:821px;top:4920px;width:178px;height:46px;font-size:14px">Subscribe</div>

<!-- FOOTER -->
<div class="abs" style="left:0;top:5048px;width:1200px;height:1px;background:#ddd"></div>
<div class="abs foot" style="left:242px;top:5090px"><h5>The Quick Links</h5><ul style="margin-top:14px"><li>Home</li><li>About Us</li><li>Audio+Video</li><li>Networking+Communication</li><li>Electronic Security</li></ul></div>
<div class="abs foot" style="left:511px;top:5090px"><h5>Contact Us</h5></div>
<svg class="abs" style="left:511px;top:5135px" width="18" height="22" viewBox="0 0 18 22"><path d="M9 1 C4 1 1 5 1 9 C1 14 9 21 9 21 C9 21 17 14 17 9 C17 5 14 1 9 1 Z" fill="none" stroke="#333" stroke-width="1.6"/><circle cx="9" cy="9" r="3" fill="none" stroke="#333" stroke-width="1.6"/></svg>
<div class="abs" style="left:542px;top:5136px;width:200px;font-size:12px;line-height:1.7">Lorem ipsum is simply dummy text Lorem Ipsum Is Simply.</div>
<svg class="abs" style="left:511px;top:5188px" width="20" height="16" viewBox="0 0 20 16"><rect x="1" y="1" width="18" height="14" rx="2" fill="none" stroke="#333" stroke-width="1.6"/><path d="M1 2 L10 9 L19 2" fill="none" stroke="#333" stroke-width="1.6"/></svg>
<div class="abs" style="left:542px;top:5187px;font-size:12px">info@silverheronsystems.test</div>
<svg class="abs" style="left:511px;top:5226px" width="20" height="20" viewBox="0 0 20 20"><path d="M4 1 L8 1 L9 6 L6 8 C7 11 9 13 12 14 L14 11 L19 12 L19 16 C19 18 17 19 15 19 C7 18 2 13 1 5 C1 3 2 1 4 1 Z" fill="none" stroke="#333" stroke-width="1.5"/></svg>
<div class="abs" style="left:542px;top:5227px;font-size:12px">615.555.0142</div>
<div class="abs foot" style="left:834px;top:5090px"><h5>Social Links</h5></div>
<div class="social" style="left:834px;background:var(--rose)"></div>
<div class="social" style="left:892px;background:var(--navy)"></div>
<div class="social" style="left:956px;background:var(--cyan)"></div>
<div class="social" style="left:1018px;background:var(--red)"></div>
<div class="abs" style="left:0;top:5290px;width:1200px;text-align:center;font-size:11px">© Silver Heron Systems. All Rights Reserved.</div>

</body>
</html>
```